Option Sheet

We need a one page option sheet with a left to right reading of the five options. It should be a one sheet, multiple colors and definitive separations between options This is used in a sales consultation. Backround or colors not in option need to have the follow RGB value (5 red, 20 green, 63 blue)

We added a smaller text file, please change that point

Target Market(s)

Divorce

Industry/Entity Type

Legal

Requirements
Must have
• 1) All five options left to right
• 2)language included in sheet

```html
<!DOCTYPE html>
<html lang="en">
<head>
<meta charset="UTF-8">
<title>5 Options Divorce – Option Sheet</title>
<link href="https://fonts.googleapis.com/css2?family=Arimo:wght@400;700&family=Barlow:wght@600;700&display=swap" rel="stylesheet">
<style>
  :root {
    --navy: rgb(5, 20, 63);
    --white: #ffffff;

    --o1-tab: #00457a;
    --o1-band: #2a6a9e;
    --o1-body: #628daf;

    --o2-tab: #0d7399;
    --o2-band: #0089c2;
    --o2-body: #5ba4c0;

    --o3-tab: #2b97ae;
    --o3-band: #46b0c5;
    --o3-body: #98c9da;

    --o4-tab: #745fa5;
    --o4-band: #8b7daf;
    --o4-body: #bbafd4;

    --o5-tab: #4e5c9a;
    --o5-band: #6675b0;
    --o5-body: #8f9bc0;

    --head-font: "Barlow", "Arial Narrow", sans-serif;
    --text-font: "Arimo", Arial, sans-serif;
  }

  * { box-sizing: border-box; margin: 0; padding: 0; }

  html, body {
    width: 927px;
    height: 1200px;
    overflow: hidden;
    background: var(--navy);
  }

  .sheet {
    position: relative;
    width: 927px;
    height: 1200px;
    background: var(--navy);
    font-family: var(--text-font);
    color: var(--white);
  }

  .sheet-spine {
    position: absolute;
    left: 0;
    top: 0;
    width: 51px;
    height: 1200px;
    background: var(--navy);
  }

  .sheet-title {
    position: absolute;
    left: 25px;
    top: 601px;
    transform: translate(-50%, -50%) rotate(90deg);
    white-space: nowrap;
    font-family: var(--text-font);
    font-weight: 700;
    font-size: 28px;
    letter-spacing: -0.5px;
  }

  .option {
    position: absolute;
    left: 51px;
    width: 876px;
  }

  .option-head {
    position: relative;
    height: 34px;
  }

  .option-tab {
    position: absolute;
    left: 0;
    top: 0;
    width: 213px;
    height: 34px;
    clip-path: polygon(0 0, 204px 0, 213px 50%, 204px 100%, 0 100%);
    font-family: var(--head-font);
    font-weight: 700;
    font-size: 18px;
    line-height: 34px;
    text-align: center;
    z-index: 1;
  }

  .option-name {
    position: absolute;
    left: 0;
    top: 0;
    width: 100%;
    height: 34px;
    font-family: var(--head-font);
    font-weight: 700;
    font-size: 18px;
    line-height: 34px;
    padding-left: 409px;
  }

  .option-body {
    position: relative;
  }

  .col {
    position: absolute;
    top: 6px;
  }
  .col-pros { left: 33px; width: 420px; }
  .col-cons { left: 432px; width: 440px; }

  .col-label {
    font-weight: 700;
    font-size: 15px;
    line-height: 20px;
  }

  .points {
    list-style: none;
    font-size: 15px;
    line-height: 20.3px;
  }
  .points li {
    position: relative;
    padding-left: 20px;
  }
  .points li::before {
    content: "";
    position: absolute;
    left: 3px;
    top: 8px;
    width: 4px;
    height: 4px;
    border-radius: 50%;
    background: var(--white);
  }
  .col-pros .points { width: 380px; }
  .col-pros .points li.narrow { width: 350px; }

  /* option 1 */
  .option-1 { top: 0; }
  .option-1 .option-tab { background: var(--o1-tab); }
  .option-1 .option-head { background: var(--o1-band); }
  .option-1 .option-body { background: var(--o1-body); height: 137px; }

  /* option 2 */
  .option-2 { top: 170px; }
  .option-2 .option-tab { background: var(--o2-tab); }
  .option-2 .option-head { background: var(--o2-band); }
  .option-2 .option-name { padding-left: 417px; }
  .option-2 .option-body { background: var(--o2-body); height: 180px; }
  .option-2 .col-cons { left: 420px; top: 8px; width: 452px; }

  /* option 3 */
  .option-3 { top: 384px; }
  .option-3 .option-tab { background: var(--o3-tab); }
  .option-3 .option-head { background: var(--o3-band); }
  .option-3 .option-name { padding-left: 442px; }
  .option-3 .option-body { background: var(--o3-body); height: 223px; }

  /* option 4 */
  .option-4 { top: 641px; }
  .option-4 .option-tab { background: var(--o4-tab); }
  .option-4 .option-head { background: var(--o4-band); }
  .option-4 .option-name { padding-left: 402px; }
  .option-4 .option-body { background: var(--o4-body); height: 192px; }
  .option-4 .col-pros { left: 34px; }
  .option-4 .col-pros .points li { width: 272px; }
  .option-4 .col-cons { left: 433px; top: 14px; }

  /* option 5 */
  .option-5 { top: 867px; }
  .option-5 .option-tab { background: var(--o5-tab); }
  .option-5 .option-head { background: var(--o5-band); }
  .option-5 .option-name { padding-left: 480px; }
  .option-5 .option-body { background: var(--o5-body); height: 299px; }
  .option-5 .col-cons { left: 437px; top: 7px; }
  .option-5 .col-cons .col-label,
  .option-5 .col-cons .points { font-size: 16px; line-height: 22px; }
  .option-5 .col-cons .points li { padding-left: 26px; }
  .option-5 .col-cons .points li::before { top: 9px; }
</style>
</head>
<body>
<main class="sheet">
  <aside class="sheet-spine">
    <h1 class="sheet-title">5 Options Divorce</h1>
  </aside>

  <section class="option option-1">
    <header class="option-head">
      <div class="option-tab">Option #1</div>
      <h2 class="option-name">Do Nothing</h2>
    </header>
    <div class="option-body">
      <div class="col col-pros">
        <p class="col-label">Advantages:</p>
        <ul class="points">
          <li>Stay married</li>
          <li>No life Changes</li>
        </ul>
      </div>
      <div class="col col-cons">
        <p class="col-label">Disadvantages:</p>
        <ul class="points">
          <li>Remain unhappy, depressed, anxious</li>
          <li>Feel unsafe</li>
          <li>Money and assets may disappear</li>
          <li>Spouse may threaten to leave and/or divorce you</li>
          <li>May cause children to be confused</li>
        </ul>
      </div>
    </div>
  </section>

  <section class="option option-2">
    <header class="option-head">
      <div class="option-tab">Option #2</div>
      <h2 class="option-name">Go to Counseling</h2>
    </header>
    <div class="option-body">
      <div class="col col-pros">
        <p class="col-label">Advantages:</p>
        <ul class="points">
          <li>Reconcile Marriage</li>
          <li>&nbsp;Help make a better life</li>
        </ul>
      </div>
      <div class="col col-cons">
        <p class="col-label">Disadvantages:</p>
        <ul class="points">
          <li>&nbsp;Past issues are highlighted and may drudge up old wounds</li>
          <li>It may just clarify the reasons you need to separate and/or divorce</li>
          <li>There is no quick fix for any situation and BOTH parties must be invested and willing to participate</li>
          <li>Bringing a third party into the marriage may cause more confusion and possible distrust</li>
        </ul>
      </div>
    </div>
  </section>

  <section class="option option-3">
    <header class="option-head">
      <div class="option-tab">Option #3</div>
      <h2 class="option-name">Do it Yourself</h2>
    </header>
    <div class="option-body">
      <div class="col col-pros">
        <p class="col-label">Advantages:</p>
        <ul class="points">
          <li>No attorney fees</li>
        </ul>
      </div>
      <div class="col col-cons">
        <p class="col-label">Disadvantages:</p>
        <ul class="points">
          <li>People often find that what is “fair,” may in fact, not be truly fair</li>
          <li>Often times, people do not know the risks</li>
          <li>Complicated legal system</li>
          <li>Unsure how to complete the necessary paperwork and meet the deadlines</li>
          <li>You are too emotional and may be unable to remain clear-headed</li>
          <li>It can be very stressful</li>
        </ul>
      </div>
    </div>
  </section>

  <section class="option option-4">
    <header class="option-head">
      <div class="option-tab">Option #4</div>
      <h2 class="option-name">Limited Representation</h2>
    </header>
    <div class="option-body">
      <div class="col col-pros">
        <p class="col-label">Advantages:</p>
        <ul class="points">
          <li>Balance between going alone and our limited involvement in the case</li>
        </ul>
      </div>
      <div class="col col-cons">
        <p class="col-label">Disadvantages:</p>
        <ul class="points">
          <li>&nbsp;Our terms may not benefit from our legal knowledge</li>
          <li>The legal consequences of your legal documents will not be explained to you so that you</li>
          <li>can formulate a plan for handling the rest of your case.</li>
          <li>&nbsp;Your spouse or other parties may cause your legal fees to increase significantly without</li>
          <li>action on your part</li>
        </ul>
      </div>
    </div>
  </section>

  <section class="option option-5">
    <header class="option-head">
      <div class="option-tab">Option #5</div>
      <h2 class="option-name">Hire Us</h2>
    </header>
    <div class="option-body">
      <div class="col col-pros">
        <p class="col-label">Advantages:</p>
        <ul class="points">
          <li>Provide peace of mind</li>
          <li>Often saves you money in the long run</li>
          <li>Can stop problems before they start and advise how actions/events may impact your</li>
          <li>case</li>
          <li class="narrow">May be able to come to a settlement agreement sooner</li>
          <li class="narrow">Lessen the emotional stress of one of the worst things that can happen to a person</li>
          <li>Inform you of your rights and what you are entitled to</li>
          <li>Save you time and energy</li>
          <li>&nbsp;Gain the full benefits of our experience</li>
          <li>&nbsp;Provide a shoulder to lean on and a sounding board</li>
        </ul>
      </div>
      <div class="col col-cons">
        <p class="col-label">Disadvantages:</p>
        <ul class="points">
          <li>Cost</li>
        </ul>
      </div>
    </div>
  </section>
</main>
</body>
</html>
```